Business Card- Occupational Therapist

I need business cards for Bright Harbour KidMotion, I am an Occupational Therapist offering child centred play therapy.
I am a sole private practitioner offering play therapy services to families in rural Great Southern region of WA, my mission statement is "helping rural children and communities thrive"
This is a new business so I am needing to promote the value of child centred play therapy within the community, and my referrers (target audience) will be: rural GPs (doctors), child health nurse, schools, disability providers, child protection workers etc) but also the families of young children in rural areas.
Target Market(s)
Families of children
Referrers (Doctors, child health nurse, schools, disability providers, child protection workers)
Industry/Entity Type
Mental Health
Contact Information for Business Card
Maren Koltwick
Occupational Therapist
Phone: 0471 828 305
Email: maren@bhkidmotion.com.au
PO Box 71 | WENDARRIN WA 6418
Requirements
Must have
- Include Bright Harbour KidMotion logo and my contact details.
Include my credentials as an Occupational Therapist and Child Centred Play Therapist
Nice to have
- "Play is a child's language and toys are their words" Dorian Welkmore

```html
<!DOCTYPE html>
<html lang="en">
<head>
<meta charset="utf-8">
<title>Bright Harbour KidMotion – Business Card</title>
<link href="https://fonts.googleapis.com/css2?family=Quicksand:wght@400;500&family=Arimo:wght@400;700&display=swap" rel="stylesheet">
<style>
  :root {
    --bg: #b9b9b9;
    --white: #ffffff;
    --green: #22a74a;
    --purple: #682060;
    --ink: #2e2e2e;
  }
  * { box-sizing: border-box; margin: 0; padding: 0; }
  html, body { width: 1200px; height: 788px; overflow: hidden; }
  body {
    background: var(--bg);
    position: relative;
    font-family: "Arimo", Arial, sans-serif;
  }
  .card {
    position: absolute;
    width: 540px;
    height: 310px;
    border-radius: 28px;
    overflow: hidden;
    box-shadow: 0 10px 24px rgba(0,0,0,0.25);
  }
  .card--front { left: 50px; top: 70px; background: var(--green); }
  .card--back { left: 610px; top: 400px; background: var(--purple); }

  .front-bands { position: absolute; inset: 0; }

  .brand-name {
    font-family: "Quicksand", sans-serif;
    font-weight: 400;
    line-height: 1.05;
  }
  .card--front .brand-name {
    position: absolute;
    left: 40px;
    top: 28px;
    font-size: 34px;
    color: var(--ink);
  }
  .card--front .brand-name span { display: block; padding-left: 58px; }

  .contact-block {
    position: absolute;
    left: 40px;
    top: 152px;
    color: var(--white);
  }
  .person-name { font-weight: 700; font-size: 26px; letter-spacing: 0.5px; }
  .person-role { font-size: 15px; margin-top: 2px; margin-bottom: 14px; }
  .contact-row {
    display: flex;
    align-items: center;
    gap: 10px;
    font-size: 15px;
    margin-top: 6px;
  }
  .contact-row svg { width: 18px; height: 18px; flex: none; }

  .mark-dot {
    position: absolute;
    right: 38px;
    top: 142px;
    width: 70px;
    height: 70px;
    border-radius: 50%;
    background: var(--white);
  }

  .card--back .brand-name {
    position: absolute;
    left: 0; right: 0;
    top: 70px;
    text-align: center;
    font-size: 36px;
    color: var(--white);
  }
  .card--back .brand-name span { display: block; }
  .card--back .mark-dot {
    left: 50%;
    right: auto;
    top: 178px;
    width: 76px;
    height: 76px;
    margin-left: -38px;
  }
</style>
</head>
<body>

  <section class="card card--front" aria-label="Business card front">
    <svg class="front-bands" viewBox="0 0 540 310" aria-hidden="true">
      <rect x="0" y="0" width="540" height="132" fill="var(--white)"/>
      <path d="M360 132 H540 V250 C470 250 410 215 360 132 Z" fill="var(--purple)"/>
    </svg>

    <h1 class="brand-name">Bright Harbour<span>KidMotion</span></h1>

    <div class="mark-dot" aria-hidden="true"></div>

    <div class="contact-block">
      <p class="person-name">MAREN KOLTWICK</p>
      <p class="person-role">Occupational Therapist</p>
      <p class="contact-row">
        <svg viewBox="0 0 18 18" aria-hidden="true"><circle cx="9" cy="9" r="9" fill="var(--white)"/><path d="M6 5 L7.5 5 L8.2 7 L7.2 7.8 C7.7 9 8.8 10.2 10.2 10.8 L11 9.8 L13 10.5 L13 12 C10 12.5 5.5 8.5 6 5 Z" fill="var(--purple)"/></svg>
        0471 828 305
      </p>
      <p class="contact-row">
        <svg viewBox="0 0 18 18" aria-hidden="true"><circle cx="9" cy="9" r="9" fill="var(--white)"/><rect x="4.5" y="6" width="9" height="6.5" fill="var(--purple)"/><path d="M4.5 6 L9 9.6 L13.5 6" fill="none" stroke="var(--white)" stroke-width="0.9"/></svg>
        maren@bhkidmotion.com.au
      </p>
      <p class="contact-row">
        <svg viewBox="0 0 18 18" aria-hidden="true"><circle cx="9" cy="9" r="9" fill="var(--white)"/><path d="M9 3.8 C6.8 3.8 5.4 5.4 5.4 7.3 C5.4 9.8 9 14 9 14 C9 14 12.6 9.8 12.6 7.3 C12.6 5.4 11.2 3.8 9 3.8 Z" fill="var(--purple)"/><circle cx="9" cy="7.3" r="1.3" fill="var(--white)"/></svg>
        PO Box 71 | WENDARRIN WA 6418
      </p>
    </div>
  </section>

  <section class="card card--back" aria-label="Business card back">
    <h2 class="brand-name"><span>Bright Harbour</span><span>KidMotion</span></h2>
    <div class="mark-dot" aria-hidden="true"></div>
  </section>

</body>
</html>
```